Neue Etiketten für die Weinflaschen der Lorenz Stiftung
Zielgruppe
Lorenz Stiftung ist eine soziale Institution. Hier leben und arbeiten rund 170 Menschen mit einer kognitiven Beeinträchtigung. Die Zielgruppe der Weine sind Privatpersonen aus dem Umfeld. Weitere Details siehe Briefing.
Aufgabenstellung
siehe Briefing, CD-Manual, etc.

```html
<!DOCTYPE html>
<html lang="de">
<head>
<meta charset="utf-8">
<title>Lorenz Stiftung – Weinetikett Rosenhalden</title>
<link href="https://fonts.googleapis.com/css2?family=Barlow:wght@400;600;700&display=swap" rel="stylesheet">
<style>
  :root {
    --stage: #1c1a1a;
    --label-red: #b3232a;
    --label-red-dark: #8c1a20;
    --stripe-brown: #6e3a22;
    --stripe-red: #d2363a;
    --ink-light: #f3e6e2;
    --portrait-top: #6b4a3e;
    --portrait-bottom: #d9d2c8;
  }
  html, body {
    margin: 0;
    width: 1200px;
    height: 771px;
    overflow: hidden;
    background: var(--stage);
    font-family: "Barlow", sans-serif;
  }
  .canvas {
    position: relative;
    width: 1200px;
    height: 771px;
    display: flex;
    align-items: center;
    justify-content: center;
  }
  .wine-label {
    position: relative;
    width: 514px;
    height: 700px;
    background: var(--label-red);
    overflow: hidden;
    color: var(--ink-light);
  }
  .label-decor {
    position: absolute;
    inset: 0;
  }
  .foundation-name {
    position: absolute;
    top: 26px;
    left: 0;
    right: 0;
    text-align: center;
    font-size: 22px;
    font-weight: 600;
    letter-spacing: 1px;
  }
  .portrait-area {
    position: absolute;
    left: 122px;
    top: 100px;
    width: 270px;
    height: 322px;
    background: linear-gradient(170deg, var(--portrait-top) 0%, #9a7a6e 45%, var(--portrait-bottom) 100%);
    box-shadow: inset 0 0 0 6px #c9b9ad;
  }
  .wine-title {
    position: absolute;
    left: 122px;
    top: 455px;
    margin: 0;
    font-size: 42px;
    font-weight: 700;
    line-height: 1;
  }
  .wine-type {
    position: absolute;
    left: 122px;
    top: 502px;
    font-size: 26px;
    font-weight: 600;
    line-height: 1;
  }
  .vintage {
    position: absolute;
    left: 122px;
    top: 533px;
    font-size: 22px;
    font-weight: 600;
    letter-spacing: 3px;
    line-height: 1;
  }
  .alcohol {
    position: absolute;
    left: 366px;
    top: 582px;
    font-size: 14px;
    font-weight: 600;
  }
  .organic-mark {
    position: absolute;
    left: 200px;
    top: 640px;
    display: flex;
    align-items: center;
    gap: 8px;
    font-size: 15px;
    font-weight: 700;
  }
  .organic-mark .dot {
    width: 22px;
    height: 22px;
    border-radius: 50%;
    background: var(--ink-light);
  }
  .volume {
    position: absolute;
    right: 32px;
    top: 645px;
    font-size: 18px;
    font-weight: 600;
  }
</style>
</head>
<body>
<main class="canvas">
  <section class="wine-label">
    <svg class="label-decor" width="514" height="700" viewBox="0 0 514 700" role="img" aria-label="Dekoratives Muster aus diagonalen Streifen in Rot- und Brauntönen">
      <defs>
        <linearGradient id="decor-fade" x1="0" y1="0" x2="1" y2="1">
          <stop offset="0" stop-color="#b3232a" stop-opacity="0"/>
          <stop offset="0.5" stop-color="#8c3424" stop-opacity="0.75"/>
          <stop offset="1" stop-color="#6e3a22" stop-opacity="0.9"/>
        </linearGradient>
      </defs>
      <path d="M380 90 L514 40 L514 610 L60 610 L60 560 Q200 520 380 420 Z" fill="url(#decor-fade)"/>
      <path d="M0 570 Q120 545 240 590 L240 610 L0 610 Z" fill="#8c1a20"/>
    </svg>
    <div class="foundation-name">Lorenz Stiftung</div>
    <div class="portrait-area" role="img" aria-label="Gemaltes Porträt einer Frau im weißen Kleid"></div>
    <h1 class="wine-title">Rosenhalden</h1>
    <div class="wine-type">Assemblage</div>
    <div class="vintage">2020</div>
    <div class="alcohol">13% Vol</div>
    <div class="organic-mark"><span class="dot"></span>Naturwerk</div>
    <div class="volume">75cl</div>
  </section>
</main>
</body>
</html>
```